Kindle Grove Wording For Logo & Business card

I have the logo, I just need the "kindle Grove" wording to go with it, and a business card design. The only thing on the business card is the website info. We provide nature connection experiences, and bolster these efforts through writing and host a platform for community around it.

I also have an idea of what it could look like (sketch), though I'm really not sure how it would come out. I am open to the best design and happy to consider original artwork. You can see what the site is about at KindleGrove.com.

Contact Information for Business Card

The only thing on the business card is the website info and the design. I will put other messaging on the back.

Website lettering (KindleGrove.com) in Montserrat

Logo Text

Kindle Grove (letters optional)

Font styles to use
Other font styles liked:
• montserrat

```html
<!DOCTYPE html>
<html lang="en">
<head>
<meta charset="utf-8">
<title>Kindle Grove – Business Card</title>
<link href="https://fonts.googleapis.com/css2?family=Montserrat:ital,wght@0,400;0,500;0,600;1,400&display=swap" rel="stylesheet">
<style>
  :root {
    --backdrop: #342839;
    --card: #ffffff;
    --ink: #1f1f1f;
    --muted: #555555;
    --brand-purple: #9b69b0;
    --brand-orange: #ee7a18;
    --emblem-dark: #2a1a3c;
  }
  * { margin: 0; padding: 0; box-sizing: border-box; }
  html, body {
    width: 1200px;
    height: 1155px;
    overflow: hidden;
    background: var(--backdrop);
    font-family: "Montserrat", sans-serif;
  }
  .card-set {
    position: absolute;
    top: 407px;
    left: 28px;
    display: flex;
    gap: 24px;
  }
  .card {
    position: relative;
    width: 560px;
    height: 340px;
    background: var(--card);
  }
  .card-front .holder-name {
    position: absolute;
    left: 35px;
    top: 28px;
    font-size: 25px;
    font-weight: 600;
    color: var(--ink);
    letter-spacing: 0.3px;
  }
  .card-front .holder-role {
    position: absolute;
    left: 35px;
    top: 62px;
    font-size: 19px;
    font-style: italic;
    color: var(--ink);
  }
  .card-front .emblem {
    position: absolute;
    left: 35px;
    top: 182px;
    width: 124px;
    height: 124px;
    border-radius: 50%;
    background: var(--emblem-dark);
  }
  .contact-list {
    position: absolute;
    left: 296px;
    top: 210px;
    list-style: none;
  }
  .contact-list li {
    display: flex;
    align-items: center;
    gap: 9px;
    height: 28px;
    font-size: 14.5px;
    color: var(--ink);
  }
  .contact-list svg { width: 14px; height: 14px; flex: none; }
  .card-back .wordmark {
    position: absolute;
    left: 0;
    right: 0;
    top: 118px;
    text-align: center;
    font-size: 54px;
    font-weight: 500;
    color: var(--brand-purple);
    letter-spacing: 1px;
  }
  .card-back .site-url {
    position: absolute;
    left: 0;
    right: 0;
    top: 290px;
    text-align: center;
    font-size: 19px;
    color: var(--muted);
    letter-spacing: 3.5px;
  }
</style>
</head>
<body>
  <main class="card-set">
    <section class="card card-front">
      <p class="holder-name">Employee's Name</p>
      <p class="holder-role">Employee</p>
      <div class="emblem"></div>
      <ul class="contact-list">
        <li>
          <svg viewBox="0 0 24 24" aria-hidden="true"><path fill="var(--brand-orange)" d="M6.6 10.8a15.1 15.1 0 0 0 6.6 6.6l2.2-2.2a1 1 0 0 1 1-.25 11.4 11.4 0 0 0 3.6.57 1 1 0 0 1 1 1V20a1 1 0 0 1-1 1A17 17 0 0 1 3 4a1 1 0 0 1 1-1h3.5a1 1 0 0 1 1 1c0 1.25.2 2.45.57 3.57a1 1 0 0 1-.25 1z"/></svg>
          000 123-456-789
        </li>
        <li>
          <svg viewBox="0 0 24 24" aria-hidden="true"><path fill="var(--brand-orange)" d="M2 5h20v14H2z"/><path fill="none" stroke="#fff" stroke-width="1.6" d="M2 5l10 8 10-8M2 19l7-7M22 19l-7-7"/></svg>
          @www.emailaddresscom
        </li>
        <li>
          <svg viewBox="0 0 24 24" aria-hidden="true"><path fill="var(--brand-orange)" d="M12 2a7 7 0 0 0-7 7c0 5 7 13 7 13s7-8 7-13a7 7 0 0 0-7-7zm0 9.5A2.5 2.5 0 1 1 12 6.5a2.5 2.5 0 0 1 0 5z"/></svg>
          address.address.address
        </li>
      </ul>
    </section>
    <section class="card card-back">
      <p class="wordmark">Kindle Grove</p>
      <p class="site-url">kindlegrove.com</p>
    </section>
  </main>
</body>
</html>
```